Social media app sign-up flow that asks users to give personal info and connect with other apps

Design an interactive, fun, and playful sign-up flow in which you are providing information about you, your interests, and connecting with different API plug-ins such as Plazabell, Workvane, Tunequill, etc. (using the brand palette attached).

Basic wireframe, and business requirements are also attached.

Target Market(s)

Gen Z + Millennials (ages 22-40)

Font styles to use
Sans Serif

Colors
fbed22
fbee3d
fbf289

Requirements
Must have
• Forms for users to submit their info. Follow the color palette attached.

Connect with Plazabell, Connect with Workvane, Connect with Tunequill, Connect with Gatherloop buttons
Nice to have
• I like the way you can use cards to submit your information for each category. Interactive card design for providing your info
Should not have
• Basic outdated designs, long forms

```html
<!DOCTYPE html>
<html lang="en">
<head>
<meta charset="utf-8">
<title>Sign-up flow – UI Design screens</title>
<link href="https://fonts.googleapis.com/css2?family=Rubik:wght@300;400;500;700&display=swap" rel="stylesheet">
<style>
:root{
  --bg:#1c1c1c;
  --yellow:#fdc430;
  --yellow-deep:#f5b400;
  --ink:#222;
  --muted:#555;
  --line:#d8d8d8;
  --field:#f6f6f6;
  --white:#fff;
  --plazabell:#4267b2;
  --workvane:#0a77b0;
  --tunequill:#1ed760;
  --mail:#dd4b39;
  --orchard:#111;
  --tile:#f5f5f5;
}
*{box-sizing:border-box;margin:0;padding:0}
html,body{width:1200px;height:3613px;overflow:hidden}
body{background:var(--bg);font-family:"Rubik",Arial,sans-serif;position:relative;color:var(--ink)}
.screen{position:absolute;background:var(--white);overflow:hidden}
.header-shape{position:absolute;left:0;top:0}
.abs{position:absolute}
.back{position:absolute;left:26px;top:18px;width:12px;height:16px}
.title-small{position:absolute;color:var(--white);font-weight:300;font-size:25px}
.title-big{position:absolute;color:var(--white);font-weight:700;font-size:40px;letter-spacing:.3px}
.center{position:absolute;left:0;right:0;text-align:center}
.hint{font-size:14px;color:var(--muted);line-height:19px}
.field{position:absolute;background:var(--field);border:1px solid #e2e2e2;font-size:12px;color:#555;display:flex;align-items:center;padding-left:12px}
.pencil{position:absolute;right:12px;top:50%;width:14px;height:14px;transform:translateY(-50%)}
.add-more{color:var(--yellow-deep);font-size:13px;font-weight:500}
.divider{position:absolute;height:1px;background:#bbb}
.or{position:absolute;font-size:11px;color:#666;background:var(--white);padding:0 10px;left:50%;transform:translateX(-50%)}
.btn{position:absolute;height:34px;color:var(--white);font-size:12px;font-weight:500;display:flex;align-items:center}
.btn-mark{width:34px;height:100%;background:rgba(0,0,0,.18);flex:none}
.btn-label{padding-left:25px}
.btn.plazabell{background:var(--plazabell)}
.btn.workvane{background:var(--workvane)}
.btn.tunequill{background:var(--tunequill)}
.btn.mail{background:var(--mail)}
.btn.orchard{background:var(--orchard)}
.btn.primary{background:var(--yellow);justify-content:center;font-weight:400}
.avatar{position:absolute;border-radius:4px}
.tile{position:absolute;width:92px;height:92px;background:var(--tile);border-radius:10px;text-align:center}
.tile svg{margin-top:8px;width:52px;height:52px}
.tile-label{display:block;color:var(--yellow-deep);font-size:14px;font-weight:500;letter-spacing:2px;margin-top:2px}
.section-number{position:absolute;left:518px;top:1012px;font-size:130px;font-weight:700;color:#2a2f36;line-height:1}
.section-title{position:absolute;left:491px;top:1068px;font-size:58px;font-weight:700;color:var(--yellow);line-height:1}
</style>
</head>
<body>

<!-- About you -->
<section class="screen about" style="left:94px;top:1005px;width:355px;height:768px">
  <svg class="header-shape" width="355" height="220"><path d="M0 0H355V102A56 56 0 0 1 299 158H56A56 56 0 0 0 0 214Z" fill="var(--yellow)"/></svg>
  <div class="title-small" style="left:41px;top:48px">Tell me</div>
  <div class="title-big" style="left:41px;top:82px">ABOUT YOU</div>
  <p class="center hint" style="top:194px;padding:0 40px">You can start where you are and change everything you want</p>

  <div class="tile" style="left:50px;top:287px">
    <svg viewBox="0 0 52 52" fill="var(--yellow)" stroke="#1a1a1a" stroke-width="2.5" stroke-linejoin="round"><path d="M8 24L26 8L44 24"/><path d="M12 21V44H40V21"/><rect x="21" y="30" width="10" height="14"/></svg>
    <span class="tile-label">PLACES</span>
  </div>
  <div class="tile" style="left:213px;top:287px">
    <svg viewBox="0 0 52 52" fill="var(--yellow)" stroke="#1a1a1a" stroke-width="2.5" stroke-linejoin="round"><path d="M4 20L26 10L48 20L26 30Z"/><path d="M13 25V36C20 42 32 42 39 36V25L26 31Z"/><path d="M44 22V34" fill="none"/></svg>
    <span class="tile-label">SCHOOLS</span>
  </div>
  <div class="tile" style="left:50px;top:398px">
    <svg viewBox="0 0 52 52" fill="var(--yellow)" stroke="#1a1a1a" stroke-width="2.5" stroke-linejoin="round"><rect x="8" y="15" width="36" height="28" rx="2"/><path d="M19 15V9H33V15" fill="none"/><path d="M14 15V43M38 15V43" fill="none"/></svg>
    <span class="tile-label">WORK</span>
  </div>
  <div class="tile" style="left:213px;top:398px">
    <svg viewBox="0 0 52 52" fill="var(--yellow)" stroke="#1a1a1a" stroke-width="2.5" stroke-linejoin="round"><circle cx="26" cy="17" r="9"/><path d="M10 44C10 33 17 28 26 28C35 28 42 33 42 44Z"/></svg>
    <span class="tile-label">PEOPLE</span>
  </div>
  <div class="tile" style="left:50px;top:508px">
    <svg viewBox="0 0 52 52" fill="var(--yellow)" stroke="#1a1a1a" stroke-width="2.5" stroke-linejoin="round"><rect x="8" y="11" width="36" height="33" rx="2"/><path d="M8 19H44M16 7V14M36 7V14M15 27H37M15 33H37M15 39H37" fill="none"/></svg>
    <span class="tile-label">EVENTS</span>
  </div>
  <div class="tile" style="left:213px;top:508px">
    <svg viewBox="0 0 52 52" fill="var(--yellow)" stroke="#1a1a1a" stroke-width="2.5" stroke-linejoin="round"><rect x="8" y="11" width="36" height="33" rx="2"/><path d="M8 20H44M16 7V14M36 7V14M19 31L24 36L33 27" fill="none"/></svg>
    <span class="tile-label">EVENTS</span>
  </div>
  <div class="tile" style="left:50px;top:620px">
    <svg viewBox="0 0 52 52" fill="var(--yellow)" stroke="#1a1a1a" stroke-width="2.5" stroke-linejoin="round"><path d="M20 36V12L40 8V32" fill="none"/><ellipse cx="15" cy="37" rx="6" ry="5"/><ellipse cx="35" cy="33" rx="6" ry="5"/><path d="M20 18L40 14" fill="none"/></svg>
    <span class="tile-label">MUSIC</span>
  </div>
  <div class="tile" style="left:213px;top:620px">
    <svg viewBox="0 0 52 52" fill="var(--yellow)" stroke="#1a1a1a" stroke-width="2.5" stroke-linejoin="round"><circle cx="26" cy="11" r="5"/><path d="M19 26C19 20 33 20 33 26Z"/><circle cx="16" cy="30" r="5"/><circle cx="36" cy="30" r="5"/><path d="M7 46C7 38 25 38 25 46Z"/><path d="M27 46C27 38 45 38 45 46Z"/></svg>
    <span class="tile-label">TEAM</span>
  </div>
</section>

<div class="section-number">07</div>
<h1 class="section-title">UI Design screen</h1>

<!-- Enjoy events / phone -->
<section class="screen signup" style="left:493px;top:1178px;width:322px;height:695px">
  <svg class="header-shape" width="322" height="200"><path d="M0 0H322V84A56 56 0 0 1 266 140H56A56 56 0 0 0 0 196Z" fill="var(--yellow)"/></svg>
  <div class="abs" style="left:37px;top:34px;color:var(--white);font-weight:500;font-size:23px;line-height:30px">Enjoy events nearby<br>and meet new<br>friends</div>
  <div class="center" style="top:166px;font-size:18px;font-weight:500">What’s your number?</div>
  <div class="center" style="top:193px;font-size:13px;color:#444">We’ll text code to verify this number</div>
  <div class="field" style="left:37px;top:231px;width:53px;height:35px;padding-left:6px">
    <svg width="26" height="18" viewBox="0 0 26 18"><rect width="26" height="18" fill="#2b3f8c"/><path d="M0 0L26 18M26 0L0 18" stroke="#fff" stroke-width="4"/><path d="M0 0L26 18M26 0L0 18" stroke="#c8102e" stroke-width="1.5"/><path d="M13 0V18M0 9H26" stroke="#fff" stroke-width="6"/><path d="M13 0V18M0 9H26" stroke="#c8102e" stroke-width="3"/></svg>
    <svg width="10" height="6" style="margin-left:5px"><path d="M0 0H10L5 6Z" fill="#555"/></svg>
  </div>
  <div class="field" style="left:100px;top:231px;width:181px;height:35px;color:#aaa">01-2345-678-0</div>
  <div class="btn primary" style="left:37px;top:282px;width:244px;height:35px">Continue</div>
  <div class="divider" style="left:37px;top:352px;width:244px"></div>
  <span class="or" style="top:344px">or</span>
  <div class="btn mail" style="left:37px;top:374px;width:244px"><span class="btn-mark"></span><span class="btn-label">Continue with E-mail</span></div>
  <div class="btn plazabell" style="left:37px;top:419px;width:244px"><span class="btn-mark"></span><span class="btn-label">Continue with Plazabell</span></div>
  <div class="btn orchard" style="left:37px;top:465px;width:244px"><span class="btn-mark"></span><span class="btn-label">Continue with Orchardly</span></div>
  <div class="btn workvane" style="left:37px;top:510px;width:244px"><span class="btn-mark"></span><span class="btn-label">Continue with Workvane</span></div>
  <p class="center" style="top:580px;font-size:10px;line-height:17px;color:#444;padding:0 30px">By signing up you accept the <span style="color:var(--yellow-deep)">Terms of Service</span> and <span style="color:var(--yellow-deep)">Privacy Policy</span></p>
  <div class="center" style="top:634px;font-size:11px;color:#333">Already have an account? <span style="color:var(--yellow-deep)">Log in</span></div>
</section>

<!-- Music -->
<section class="screen music" style="left:843px;top:1178px;width:322px;height:695px">
  <svg class="header-shape" width="322" height="200"><path d="M0 0H322V84A56 56 0 0 1 266 140H56A56 56 0 0 0 0 196Z" fill="var(--yellow)"/></svg>
  <svg class="back" viewBox="0 0 12 16"><path d="M9 2L3 8L9 14" stroke="#fff" stroke-width="1.5" fill="none"/></svg>
  <div class="title-big" style="left:37px;top:45px">MUSIC</div>
  <div class="title-small" style="left:37px;top:91px;font-size:23px">You love</div>
  <div class="center" style="top:184px;font-size:13px;color:#444">Fill out manually</div>
  <div class="avatar" role="img" aria-label="Artist photo" style="left:37px;top:217px;width:55px;height:53px;background:linear-gradient(135deg,#b9b9b9,#5a5a5a)"></div>
  <div class="field" style="left:99px;top:217px;width:182px;height:53px">Marlo Vance<svg class="pencil" viewBox="0 0 14 14"><path d="M2 12L3 9L10 2L12 4L5 11Z" fill="var(--yellow)"/></svg></div>
  <div class="avatar" role="img" aria-label="Band photo" style="left:37px;top:286px;width:55px;height:55px;background:linear-gradient(135deg,#8a8a8a,#2a2a2a)"></div>
  <div class="field" style="left:99px;top:286px;width:182px;height:55px">The Larkfields<svg class="pencil" viewBox="0 0 14 14"><path d="M2 12L3 9L10 2L12 4L5 11Z" fill="var(--yellow)"/></svg></div>
  <div class="center add-more" style="top:360px">+ Add More Here</div>
  <div class="divider" style="left:37px;top:440px;width:244px"></div>
  <span class="or" style="top:432px">or</span>
  <p class="center hint" style="top:463px;font-size:13px;padding:0 40px">Fill out automatically with your social media profile</p>
  <div class="btn plazabell" style="left:37px;top:517px;width:244px"><span class="btn-mark"></span><span class="btn-label">Connect with Plazabell</span></div>
  <div class="btn tunequill" style="left:37px;top:576px;width:244px"><span class="btn-mark"></span><span class="btn-label">Connect with Tunequill</span></div>
</section>

<!-- People -->
<section class="screen people" style="left:94px;top:1809px;width:355px;height:768px">
  <svg class="header-shape" width="355" height="215"><path d="M0 0H355V98A56 56 0 0 1 299 154H56A56 56 0 0 0 0 210Z" fill="var(--yellow)"/></svg>
  <svg class="back" viewBox="0 0 12 16"><path d="M9 2L3 8L9 14" stroke="#fff" stroke-width="1.5" fill="none"/></svg>
  <div class="title-big" style="left:41px;top:52px">PEOPLE</div>
  <div class="title-small" style="left:41px;top:100px">You know</div>
  <p class="center hint" style="top:196px;padding:0 60px">Fill out automatically with your social media profile</p>
  <div class="btn plazabell" style="left:41px;top:268px;width:272px;height:36px"><span class="btn-mark"></span><span class="btn-label" style="padding-left:36px;font-size:13px;font-weight:400">Sync with Plazabell</span></div>
  <div class="divider" style="left:18px;top:351px;width:315px"></div>
  <div class="avatar" role="img" aria-label="Friend photo" style="left:18px;top:381px;width:86px;height:86px;background:linear-gradient(135deg,#6b1d1d,#2a0d0d)"></div>
  <div class="avatar" role="img" aria-label="Friend photo" style="left:133px;top:381px;width:86px;height:86px;background:linear-gradient(135deg,#8a98a8,#3c4652)"></div>
  <div class="avatar" role="img" aria-label="Friend photo" style="left:249px;top:381px;width:86px;height:86px;background:linear-gradient(135deg,#9a6a3a,#4a2e18)"></div>
  <div class="avatar" role="img" aria-label="Friend photo" style="left:18px;top:492px;width:86px;height:86px;background:linear-gradient(135deg,#f0d060,#2a3a6a)"></div>
  <div class="avatar" role="img" aria-label="Friend photo" style="left:133px;top:492px;width:86px;height:86px;background:linear-gradient(135deg,#f4f1ec,#d9b79a)"></div>
  <div class="avatar" role="img" aria-label="Friend photo" style="left:249px;top:492px;width:86px;height:86px;background:linear-gradient(135deg,#3a6a6a,#1a2a30)"></div>
  <div class="avatar" role="img" aria-label="Friend photo" style="left:18px;top:603px;width:86px;height:86px;background:linear-gradient(135deg,#b89a7a,#6a4a3a)"></div>
  <div class="avatar" role="img" aria-label="Friend photo" style="left:133px;top:603px;width:86px;height:86px;background:linear-gradient(135deg,#2ec27e,#1b8a55)"></div>
  <div class="avatar" role="img" aria-label="Friend photo" style="left:249px;top:603px;width:86px;height:86px;background:linear-gradient(135deg,#d88a2a,#5a3010)"></div>
  <div class="avatar" role="img" aria-label="Friend photo" style="left:18px;top:715px;width:86px;height:86px;background:linear-gradient(135deg,#3a4a50,#141a1c)"></div>
  <div class="avatar" role="img" aria-label="Friend photo" style="left:133px;top:715px;width:86px;height:86px;background:linear-gradient(135deg,#6a8a4a,#c0503a)"></div>
  <div class="avatar" role="img" aria-label="Friend photo" style="left:249px;top:715px;width:86px;height:86px;background:linear-gradient(135deg,#8a1a2a,#3a0a10)"></div>
</section>

<!-- Place -->
<section class="screen place" style="left:493px;top:1909px;width:322px;height:697px">
  <svg class="header-shape" width="322" height="200"><path d="M0 0H322V84A56 56 0 0 1 266 140H56A56 56 0 0 0 0 196Z" fill="var(--yellow)"/></svg>
  <svg class="back" viewBox="0 0 12 16"><path d="M9 2L3 8L9 14" stroke="#fff" stroke-width="1.5" fill="none"/></svg>
  <div class="title-big" style="left:37px;top:45px">PLACE</div>
  <div class="title-small" style="left:37px;top:91px;font-size:23px">You’ve lived</div>
  <div class="center" style="top:183px;font-size:13px;color:#444">Fill out manually</div>
  <div class="field" style="left:37px;top:218px;width:246px;height:36px">Chicago<svg class="pencil" viewBox="0 0 14 14"><path d="M2 12L3 9L10 2L12 4L5 11Z" fill="var(--yellow)"/></svg></div>
  <div class="field" style="left:37px;top:269px;width:246px;height:36px">Madrid<svg class="pencil" viewBox="0 0 14 14"><path d="M2 12L3 9L10 2L12 4L5 11Z" fill="var(--yellow)"/></svg></div>
  <div class="field" style="left:37px;top:322px;width:246px;height:36px">London<svg class="pencil" viewBox="0 0 14 14"><path d="M2 12L3 9L10 2L12 4L5 11Z" fill="var(--yellow)"/></svg></div>
  <div class="center add-more" style="top:379px">+ Add More Here</div>
  <div class="divider" style="left:37px;top:440px;width:246px"></div>
  <span class="or" style="top:432px">or</span>
  <p class="center hint" style="top:465px;font-size:13px;padding:0 40px">Fill out automatically with your social media profile</p>
  <div class="btn plazabell" style="left:37px;top:519px;width:246px"><span class="btn-mark"></span><span class="btn-label">Connect with Plazabell</span></div>
  <div class="btn workvane" style="left:37px;top:578px;width:246px"><span class="btn-mark"></span><span class="btn-label">Connect with Workvane</span></div>
</section>

<!-- School -->
<section class="screen school" style="left:843px;top:1909px;width:322px;height:697px">
  <svg class="header-shape" width="322" height="200"><path d="M0 0H322V84A56 56 0 0 1 266 140H56A56 56 0 0 0 0 196Z" fill="var(--yellow)"/></svg>
  <svg class="back" viewBox="0 0 12 16"><path d="M9 2L3 8L9 14" stroke="#fff" stroke-width="1.5" fill="none"/></svg>
  <div class="title-big" style="left:37px;top:45px">SCHOOL</div>
  <div class="title-small" style="left:37px;top:91px;font-size:23px">You’ve attended</div>
  <div class="center" style="top:183px;font-size:13px;color:#444">Fill out manually</div>
  <div class="field" style="left:37px;top:218px;width:246px;height:69px;display:block;padding-top:12px;line-height:15px">
    <div style="font-weight:500;color:#333">Brookhaven University</div>
    <div>Bachelor’s degree, Information Technology</div>
    <div style="font-size:10px;color:#888">2015-2019</div>
  </div>
  <div class="center add-more" style="top:304px">+ Add More Here</div>
  <div class="divider" style="left:37px;top:442px;width:246px"></div>
  <span class="or" style="top:434px">or</span>
  <p class="center hint" style="top:465px;font-size:13px;padding:0 40px">Fill out automatically with your social media profile</p>
  <div class="btn workvane" style="left:37px;top:520px;width:246px"><span class="btn-mark"></span><span class="btn-label">Connect with Workvane</span></div>
</section>

<!-- Sport team -->
<section class="screen sport" style="left:94px;top:2671px;width:355px;height:768px">
  <svg class="header-shape" width="355" height="215"><path d="M0 0H355V98A56 56 0 0 1 299 154H56A56 56 0 0 0 0 210Z" fill="var(--yellow)"/></svg>
  <svg class="back" viewBox="0 0 12 16"><path d="M9 2L3 8L9 14" stroke="#fff" stroke-width="1.5" fill="none"/></svg>
  <div class="title-small" style="left:35px;top:48px">Your favourite</div>
  <div class="title-big" style="left:35px;top:82px">SPORT TEAM</div>
  <div class="center" style="top:201px;font-size:14px;color:#444">Fill out manually</div>
  <div class="field" style="left:43px;top:254px;width:58px;height:39px;padding-left:8px">
    <svg width="24" height="24" viewBox="0 0 24 24"><circle cx="12" cy="12" r="10" fill="var(--yellow)"/><path d="M2 12H22M12 2V22M5 5C9 9 9 15 5 19M19 5C15 9 15 15 19 19" stroke="#fff" stroke-width="1.4" fill="none"/></svg>
    <svg width="10" height="6" style="margin-left:6px"><path d="M0 0H10L5 6Z" fill="#555"/></svg>
  </div>
  <div class="field" style="left:111px;top:254px;width:203px;height:39px;font-size:13px;color:#333;padding-left:16px">Choose league<svg style="position:absolute;right:12px;top:16px" width="11" height="7"><path d="M0 0H11L5.5 7Z" fill="#555"/></svg></div>
  <div class="field" style="left:43px;top:307px;width:271px;height:39px;font-size:13px">Location</div>
  <div class="field" style="left:43px;top:363px;width:271px;height:39px;font-size:13px">Official team name here...</div>
  <div class="btn primary" style="left:41px;top:672px;width:270px;height:39px;font-size:13px">Save</div>
</section>

</body>
</html>
```